Creating a Label for a new CBD Vape Line call "Brizel".

This will be a project that will create the first label design on a BRIZEL Vape product that is being rolled out in Colorado. The vape line will cater to high concentration CBD Vape sold in disposable vape pens and replacement cartridge's. In the sea of vape pens we want our packaging to stand out with a bold, bright, clean, abstract design that will highlight the brand "BRIZEL" in a font that stands out and is quickly recognized. The target demographic for this line is 18-29 years of age. The mock up of the brizel vape picture does not meet our marketing desire, I just wanted to show you the approximate shape and size of the label and that the font used for the label will be added to the actual pen. This pen will have 100% CBD, cut with all natural terpenes with no need for chemicals like PG or VG, not many on the market like that. I included several marketing logos that caught our eye with other type product, please look at those as examples but we are open to creativity.

Target Market(s)

18-29 year old

Industry/Entity Type

CBD and Vape

Font styles to use
Serif
Sans Serif

Requirements
Must have
• bold, colorful, fun, eye catching
Nice to have
• Several brand ideas presented to give the flavor of the marketing. The example font on the prototype is not 'cool enough' to use, we'd like that name BRIZEL to look and feel brizzzel. :-)
Should not have
• old school, boring, dull colors, small font

```html
<!DOCTYPE html>
<html lang="en">
<head>
<meta charset="utf-8">
<title>Brizel High Concentration CBD Vape Label</title>
<link rel="stylesheet" href="https://fonts.googleapis.com/css2?family=Archivo+Black&family=Arimo:wght@400;700&family=Tinos:wght@400;700&display=swap">
<style>
  :root {
    --bg-center: #ffffff;
    --bg-edge: #a9e3fb;
    --label-white: #ffffff;
    --tag-blue: #1592ea;
    --brand-pink: #e8508f;
    --pink-mid: #ee76a8;
    --lavender: #b48ccc;
    --blue-base: #4f86dc;
    --ink: #141414;
    --wave-blue: #3f8ee6;
    --wave-pink: #f07fb4;
  }
  html, body {
    margin: 0;
    padding: 0;
    width: 1200px;
    height: 1200px;
    overflow: hidden;
  }
  body {
    background: radial-gradient(circle at 50% 50%, var(--bg-center) 35%, var(--bg-edge) 100%);
    position: relative;
  }
  .label {
    position: absolute;
    left: 420px;
    top: 80px;
    width: 360px;
    height: 1040px;
    background: linear-gradient(180deg,
      var(--label-white) 0%,
      var(--label-white) 48%,
      #f9dbe8 56%,
      var(--pink-mid) 66%,
      var(--lavender) 78%,
      var(--blue-base) 100%);
    overflow: hidden;
    box-shadow: 0 6px 24px rgba(60, 120, 170, 0.18);
  }
  .age-tag {
    position: absolute;
    left: 31px;
    top: 0;
    width: 71px;
    height: 143px;
    background: var(--tag-blue);
    color: var(--label-white);
    font-family: "Arimo", Arial, sans-serif;
    font-weight: 700;
    font-size: 15px;
    display: flex;
    align-items: center;
    justify-content: center;
  }
  .brand-name {
    position: absolute;
    left: 0;
    right: 0;
    top: 262px;
    margin: 0;
    text-align: center;
    font-family: "Archivo Black", "Arial Black", sans-serif;
    font-weight: 400;
    font-size: 62px;
    letter-spacing: 2px;
    line-height: 1;
    color: var(--brand-pink);
  }
  .product-line {
    position: absolute;
    left: 0;
    right: 0;
    top: 348px;
    text-align: center;
    font-family: "Tinos", "Times New Roman", serif;
    color: var(--ink);
  }
  .product-line .concentration {
    display: block;
    font-size: 27px;
    line-height: 1.2;
  }
  .product-line .format {
    display: block;
    font-size: 27px;
    line-height: 1.3;
  }
  .product-line .format strong {
    font-size: 38px;
    font-weight: 700;
  }
  .net-weight {
    position: absolute;
    left: 0;
    right: 0;
    top: 706px;
    text-align: center;
    font-family: "Arimo", Arial, sans-serif;
    font-size: 15px;
    color: var(--label-white);
  }
  .web-address {
    position: absolute;
    left: 0;
    right: 0;
    top: 732px;
    text-align: center;
    font-family: "Arimo", Arial, sans-serif;
    font-weight: 700;
    font-size: 28px;
    color: var(--ink);
  }
  .wave-band {
    position: absolute;
    left: 0;
    width: 360px;
    top: 790px;
    height: 160px;
    background: linear-gradient(100deg,
      var(--wave-blue) 0%,
      var(--wave-pink) 40%,
      #8f9ee4 65%,
      var(--wave-pink) 85%,
      var(--wave-blue) 100%);
    opacity: 0.75;
  }
</style>
</head>
<body>
  <main class="label">
    <div class="age-tag">21 YRS+</div>
    <h1 class="brand-name">BRIZEL</h1>
    <p class="product-line">
      <span class="concentration">High Concentration</span>
      <span class="format"><strong>CBD</strong> Vape</span>
    </p>
    <div class="net-weight">NET WT 30ML</div>
    <div class="web-address">BrizelCBD.com</div>
    <div class="wave-band" role="img" aria-label="Flowing abstract wave lines in blue and pink"></div>
  </main>
</body>
</html>
```